Gold Finch Print and Mailing Services

We are looking for a website layout design for a direct print and mailing company which prints graphics, post cards, letters, does mailing and more.

Please see attached logo, as it will be used to match color scheme of website.

Current website:
www.goldfinchprintpost.example

Websites we like:
https://velmorepress.example

Target Market(s)

Businesses / Media

Number of Pages Required

3 page

Font styles to use
Sans Serif

Requirements
Must have
• Color scheme to match logo

```html
<!DOCTYPE html>
<html lang="en">
<head>
<meta charset="utf-8">
<title>Gold Finch Print and Mailing Services</title>
<link href="https://fonts.googleapis.com/css2?family=Ubuntu:wght@400;500;700&family=Mulish:wght@400;600&display=swap" rel="stylesheet">
<style>
:root{
  --pink:#e8236c;
  --blue:#1b66ad;
  --cyan:#1a9bd7;
  --orange:#f4a53a;
  --ink:#444;
  --muted:#8a8a8a;
  --grey-band:#efefef;
  --footer:#333;
  --white:#fff;
}
*{margin:0;padding:0;box-sizing:border-box}
html,body{width:1200px;height:3579px;overflow:hidden}
body{position:relative;background:var(--white);font-family:"Mulish",sans-serif;color:var(--ink)}
.abs{position:absolute}
h2.section-title{position:absolute;left:0;width:1200px;text-align:center;font-family:"Ubuntu",sans-serif;font-weight:700;font-size:33px;color:#4a4a4a;letter-spacing:1px}

/* header */
.site-header{position:absolute;left:0;top:0;width:1200px;height:148px;background:var(--white);z-index:3}
.brand{position:absolute;left:84px;top:40px;display:flex;align-items:center;gap:10px;font-family:"Ubuntu",sans-serif;font-weight:700;font-size:22px;color:var(--blue)}
.brand-dot{width:18px;height:18px;border-radius:50%;background:var(--pink)}
.contact-block{position:absolute;top:26px;display:flex;align-items:center;gap:14px;font-family:"Ubuntu",sans-serif;font-size:19px;color:#666;line-height:28px}
.contact-block a{color:var(--pink);text-decoration:underline}
.ring{width:56px;height:56px;border:2px solid var(--pink);border-radius:50%;display:flex;align-items:center;justify-content:center}
.main-nav{position:absolute;left:79px;top:122px;width:1042px;height:48px;background:var(--blue);display:flex;align-items:center;padding-left:26px;gap:31px;font-family:"Ubuntu",sans-serif;font-size:16px;color:var(--white);z-index:4}

/* hero */
.hero{position:absolute;left:0;top:148px;width:1200px;height:561px;background:linear-gradient(100deg,#f3ece9 0%,#e9d9e2 30%,#c9c6cf 55%,#8ea0b7 75%,#e7e3e8 100%)}
.hero-title{position:absolute;left:79px;top:216px;font-family:"Ubuntu",sans-serif;font-weight:700;font-size:33px;line-height:48px;color:#222;letter-spacing:1px}

/* welcome */
.welcome-text{position:absolute;left:200px;top:811px;width:800px;text-align:center;font-size:14.5px;line-height:24px;color:#666}
.btn{position:absolute;left:511px;top:930px;width:176px;height:48px;background:var(--pink);color:var(--white);font-family:"Ubuntu",sans-serif;font-weight:500;font-size:18px;display:flex;align-items:center;justify-content:center}

/* services */
.band{position:absolute;left:0;width:1200px;background:var(--grey-band)}
.service-card{position:absolute;width:239px;height:188px}
.service-card .caption{position:absolute;left:0;bottom:0;width:100%;height:44px;background:rgba(30,30,30,.75);color:var(--white);font-size:15px;display:flex;align-items:center;padding-left:12px}
.service-card svg{position:absolute;right:0;bottom:0}

/* capabilities */
.cap-photo{position:absolute;left:0;top:1627px;width:560px;height:604px;background:linear-gradient(90deg,#d24a6a 0%,#e8845a 30%,#e9c9a8 60%,rgba(255,255,255,0) 100%)}
.cap-item{position:absolute}
.cap-icon{position:absolute;left:0;top:0;width:93px;height:91px;display:flex;align-items:center;justify-content:center}
.cap-body{position:absolute;left:124px;top:4px;width:520px}
.cap-body h3{font-family:"Ubuntu",sans-serif;font-weight:400;font-size:21px;line-height:28px}
.cap-body p{font-size:15px;line-height:23px;color:#666;margin-top:4px}
.cap-body .more{font-size:15px;color:var(--cyan);margin-top:2px}

/* news */
.news-card{position:absolute;top:2334px;width:324px;height:341px;background:var(--white)}
.news-card .thumb{width:324px;height:220px}
.news-card .date{position:absolute;left:17px;top:154px;width:78px;height:92px;background:var(--pink);color:var(--white);text-align:center;font-family:"Ubuntu",sans-serif}
.news-card .date b{display:block;font-size:33px;font-weight:500;margin-top:12px}
.news-card .date span{font-size:16px}
.news-card p{position:absolute;left:20px;top:262px;width:280px;font-size:16px;line-height:26px;color:#555}

/* faq */
.faq-list{position:absolute;left:79px;top:2862px;width:529px}
.faq-item{border-bottom:1px solid #ddd;padding:12px 0 14px;display:block}
.faq-q{display:flex;align-items:center;gap:12px;font-size:17px;color:#555}
.faq-a{font-size:14px;line-height:22px;color:#999;margin:14px 0 4px}
.toggle{width:20px;height:20px;border:1.5px solid #777;border-radius:50%;position:relative;flex:none}
.toggle::before{content:"";position:absolute;left:4px;top:8px;width:9px;height:1.5px;background:#777}
.toggle.plus::after{content:"";position:absolute;left:8px;top:4px;width:1.5px;height:9px;background:#777}
.postcards{position:absolute;left:664px;top:2870px;width:460px;height:400px;background:linear-gradient(150deg,#b9cde0 0%,#d9e3ee 40%,#f3d3dc 70%,#ffffff 100%);border-radius:4px}

/* footer */
.site-footer{position:absolute;left:0;top:3336px;width:1200px;height:243px;background:var(--footer)}
.footer-nav{position:absolute;left:0;top:150px;width:1200px;display:flex;justify-content:center;gap:30px;font-size:15px;color:#ddd}
.copyright{position:absolute;left:0;top:188px;width:1200px;text-align:center;font-size:14px;color:#ccc}
</style>
</head>
<body>

<header class="site-header">
  <div class="brand"><span class="brand-dot"></span>Gold Finch</div>
  <div class="contact-block" style="left:608px">
    <div class="ring"><svg width="26" height="26" viewBox="0 0 24 24" fill="none" stroke="#e8236c" stroke-width="2"><path d="M10 17l5-5-5-5"/><path d="M15 12H3"/><path d="M14 3h6v18h-6"/></svg></div>
    <div>Current Clients &amp;<br>New Clients: <a>Sign In</a></div>
  </div>
  <div class="contact-block" style="left:907px">
    <div class="ring"><svg width="24" height="24" viewBox="0 0 24 24" fill="none" stroke="#e8236c" stroke-width="2"><path d="M5 3h4l2 5-3 2a11 11 0 006 6l2-3 5 2v4a2 2 0 01-2 2A17 17 0 013 5a2 2 0 012-2z"/></svg></div>
    <div>Call Us Now<br>(555) 014-2290</div>
  </div>
</header>

<nav class="main-nav">
  <span>Home</span><span>About</span><span>Service &amp; Print Product</span><span>Quotes &amp; Custom Orders</span><span>My Invoice Account</span><span>News</span><span>FAQ</span><span>Contact</span>
</nav>

<section class="hero" role="img" aria-label="Colour print proof sheets with a magnifying loupe">
  <h1 class="hero-title">MASTERS OF VIBRANT<br>COLOR DIGITAL PRINT<br>AND MAILING SERVICES!</h1>
</section>

<section class="welcome">
  <h2 class="section-title" style="top:760px">WELCOME TO GOLD FINCH</h2>
  <p class="welcome-text">Even in today's digital marketplace, mail continues to be one of the most effective forms of communication. Gold Finch's mastery of the complexities of managed mail gives our clients the assurance that their mailings will be handled in the most professional, cost-effective, and efficient way possible. That means rapid results without the worry. You'll always get the optimum postage rates with our help.</p>
  <div class="btn">KNOW MORE</div>
</section>

<section class="band" style="top:1033px;height:594px">
  <h2 class="section-title" style="top:42px">SERVICES &amp; PRINT PRODUCTS</h2>
</section>
<div class="service-card" style="left:79px;top:1136px;background:linear-gradient(#9fb4c4,#6f8393)" role="img" aria-label="Lettershop machinery"><div class="caption">Lettershop services</div><svg width="24" height="44"><path d="M2 0l20 22-20 22h8l12-14V14L10 0z" fill="#e8236c"/></svg></div>
<div class="service-card" style="left:346px;top:1136px;background:linear-gradient(#2b2b2b,#6a5a4a)" role="img" aria-label="Laser printer output"><div class="caption">Laser Printing</div><svg width="24" height="44"><path d="M2 0l20 22-20 22h8l12-14V14L10 0z" fill="#1a9bd7"/></svg></div>
<div class="service-card" style="left:615px;top:1136px;background:linear-gradient(#7a9a6a,#c0584a)" role="img" aria-label="Colour digital press printing"><div class="caption">Color Digital Printing</div><svg width="24" height="44"><path d="M2 0l20 22-20 22h8l12-14V14L10 0z" fill="#e8236c"/></svg></div>
<div class="service-card" style="left:882px;top:1136px;background:linear-gradient(#d9c6a4,#b58a55)" role="img" aria-label="Packed boxes for fulfilment"><div class="caption">Fulfillment Services</div><svg width="24" height="44"><path d="M2 0l20 22-20 22h8l12-14V14L10 0z" fill="#f4a53a"/></svg></div>
<div class="service-card" style="left:210px;top:1365px;background:linear-gradient(#1f8f9b,#0d4a55)" role="img" aria-label="Digital mail on a laptop"><div class="caption">Mail List &amp; Digital Mail</div><svg width="24" height="44"><path d="M2 0l20 22-20 22h8l12-14V14L10 0z" fill="#1a9bd7"/></svg></div>
<div class="service-card" style="left:480px;top:1365px;background:linear-gradient(#6b5a44,#c9a96a)" role="img" aria-label="Sorted stacks of mail"><div class="caption">Mail Sorting</div><svg width="24" height="44"><path d="M2 0l20 22-20 22h8l12-14V14L10 0z" fill="#3bb14a"/></svg></div>
<div class="service-card" style="left:749px;top:1365px;background:linear-gradient(#f0d8e6,#c4bcd0)" role="img" aria-label="Graphic design workstation"><div class="caption">Graphic Design Services</div><svg width="24" height="44"><path d="M2 0l20 22-20 22h8l12-14V14L10 0z" fill="#e8236c"/></svg></div>

<section class="capabilities">
  <div class="cap-photo" role="img" aria-label="Spring tulips with butterflies"></div>
  <h2 class="section-title" style="left:482px;top:1678px;width:auto">CAPABILITIES</h2>
  <div class="cap-item" style="left:489px;top:1749px">
    <div class="cap-icon" style="background:var(--pink)"><svg width="54" height="54" viewBox="0 0 54 54" fill="none" stroke="#fff" stroke-width="3"><path d="M46 27A19 19 0 1127 8"/><path d="M27 3l5 5-5 5"/><text x="15" y="33" fill="#fff" stroke="none" font-family="Ubuntu,sans-serif" font-weight="700" font-size="16">24</text></svg></div>
    <div class="cap-body"><h3 style="color:var(--pink)">Access Your Art Files 24/7 with Safe Online Storage</h3><p>Safeguard your logos, flyers, forms and other designs online<br>to print any quantity, any time – on demand!</p><div class="more">READ MORE</div></div>
  </div>
  <div class="cap-item" style="left:530px;top:1902px">
    <div class="cap-icon" style="background:var(--cyan)"><svg width="50" height="46" viewBox="0 0 50 46" fill="none" stroke="#fff" stroke-width="3"><rect x="3" y="3" width="44" height="30"/><path d="M18 43h14M25 33v10"/><path d="M16 26l14-14 4 4-14 14h-4z"/></svg></div>
    <div class="cap-body"><h3 style="color:var(--blue)">Meet Our Ensemble of Graphic Designers</h3><p>See a variety of graphic design styles from talented artists,<br>all at affordable prices! Get a custom quote now.</p><div class="more">READ MORE</div></div>
  </div>
  <div class="cap-item" style="left:575px;top:2059px">
    <div class="cap-icon" style="background:var(--orange)"><svg width="50" height="46" viewBox="0 0 50 46" fill="none" stroke="#fff" stroke-width="3"><path d="M4 18L25 4l21 14v24H4z"/><path d="M4 18l21 14 21-14"/><path d="M18 20h14M20 13h10"/></svg></div>
    <div class="cap-body"><h3 style="color:var(--orange)">Grab Your Best Clients with<br>Market-Focused Mail Lists!</h3><p>Combine variable print and mail service with advanced...</p><div class="more">READ MORE</div></div>
  </div>
</section>

<section class="band" style="top:2231px;height:525px">
  <h2 class="section-title" style="top:48px">LATEST NEWS</h2>
</section>
<article class="news-card" style="left:79px"><div class="thumb" role="img" aria-label="Team reviewing colour swatches at a desk" style="background:linear-gradient(#d8d4cc,#9c9a94)"></div><div class="date"><b>17</b><span>MAY</span></div><p>Lorem Ipsum is simply dummy text of the printing and typesetting.</p></article>
<article class="news-card" style="left:439px"><div class="thumb" role="img" aria-label="Hand touching a wall of floating photos" style="background:linear-gradient(#2a3248,#7a6a80)"></div><div class="date"><b>17</b><span>MAY</span></div><p>Lorem Ipsum is simply dummy text of the printing and typesetting.</p></article>
<article class="news-card" style="left:799px"><div class="thumb" role="img" aria-label="Office lounge with dotted wall graphics" style="background:linear-gradient(#eeeae2,#c9d1b8)"></div><div class="date"><b>17</b><span>MAY</span></div><p>Lorem Ipsum is simply dummy text of the printing and typesetting.</p></article>

<section class="faq">
  <h2 class="section-title" style="top:2804px">FAQ</h2>
  <div class="faq-list">
    <div class="faq-item"><div class="faq-q"><span class="toggle"></span>What type of file must I send for print orders?</div><p class="faq-a">We can accept most types of art files. We prefer high-resolution PDFs, whereby you attach the native files, the fonts and any other special attachments that make up your art file.</p></div>
    <div class="faq-item"><div class="faq-q"><span class="toggle plus"></span>Can I order a print and not mail?</div></div>
    <div class="faq-item"><div class="faq-q"><span class="toggle plus"></span>At what DPI should my images be?</div></div>
    <div class="faq-item"><div class="faq-q"><span class="toggle plus"></span>How do I provide my files for full color digital printing?</div></div>
    <div class="faq-item"><div class="faq-q"><span class="toggle plus"></span>How do I size my artwork if it has bleeds?</div></div>
  </div>
  <div class="postcards" role="img" aria-label="Stacked illustrated postcards"></div>
</section>

<footer class="site-footer">
  <div class="abs" style="left:527px;top:35px;width:146px;height:89px;background:#f2f2f2;border:3px solid #c8102e;border-radius:4px"></div>
  <nav class="footer-nav"><span>Home</span><span>About</span><span>Service &amp; Print Product</span><span>Quotes &amp; Custom Orders</span><span>My Invoice Account</span><span>News</span><span>FAQ</span><span>Contact</span></nav>
  <p class="copyright">2018 ©Gold Finch Print and Mailing Services - All Rights Reserved.</p>
</footer>

</body>
</html>
```